The Timber Loft

We need a business card design for our wardrobe company.
Please visit our website www.zorvelcabinets.com to get an idea of who we are.

```html
<!DOCTYPE html>
<html lang="en">
<head>
<meta charset="utf-8">
<title>The Timber Loft — Business Card</title>
<link rel="stylesheet" href="https://fonts.googleapis.com/css2?family=Montserrat:wght@400;500;600;700&family=Oswald:wght@600&display=swap">
<style>
  :root {
    --backdrop: #2a2a2b;
    --card: #1d1d1e;
    --ink: #ffffff;
    --ink-muted: #8a8a8c;
    --accent: #17a8e6;
  }
  * { box-sizing: border-box; margin: 0; padding: 0; }
  html, body {
    width: 1200px; height: 895px; overflow: hidden;
    background: var(--backdrop);
    font-family: "Montserrat", Arial, sans-serif;
    color: var(--ink);
  }
  .stage {
    position: relative; width: 1200px; height: 895px;
    display: flex; align-items: center; justify-content: center; gap: 40px;
  }
  .card {
    position: relative; width: 540px; height: 310px;
    background: var(--card);
    border-radius: 16px;
    overflow: hidden;
  }

  /* Front */
  .brand {
    position: absolute; left: 92px; top: 92px;
    display: flex; align-items: center; gap: 22px;
  }
  .brand-mark {
    width: 78px; height: 78px;
    border: 2px solid var(--ink-muted);
    flex: none;
  }
  .brand-name {
    font-size: 24px; font-weight: 500; letter-spacing: 1px;
    text-transform: uppercase; color: var(--ink-muted);
    line-height: 1.2; white-space: nowrap;
  }
  .brand-tagline {
    font-size: 18px; font-weight: 500; color: var(--ink-muted);
    margin-top: 4px; white-space: nowrap;
  }
  .reg-number {
    position: absolute; left: 0; right: 0; bottom: 64px;
    text-align: center; font-size: 14px; font-weight: 700;
  }

  /* Back */
  .card-back { border-bottom: 6px solid var(--accent); }
  .identity {
    position: absolute; left: 30px; top: 104px; width: 244px;
    text-align: right;
  }
  .person-name {
    font-family: "Oswald", "Arial Narrow", sans-serif;
    font-size: 42px; font-weight: 600; letter-spacing: 1px;
    text-transform: uppercase; line-height: 1; white-space: nowrap;
  }
  .person-role {
    font-size: 17px; font-weight: 500; color: var(--accent);
    text-transform: uppercase; margin-top: 8px; white-space: nowrap;
  }
  .divider {
    position: absolute; left: 288px; top: 92px;
    width: 2px; height: 76px; background: var(--ink);
  }
  .contacts {
    position: absolute; left: 302px; top: 90px;
    list-style: none; font-size: 13.5px; line-height: 26px;
  }
  .contacts li { display: flex; align-items: center; gap: 8px; white-space: nowrap; }
  .contacts svg { width: 14px; height: 14px; flex: none; }
  .contacts .accent { color: var(--accent); }
  .address {
    position: absolute; left: 52px; bottom: 40px;
    font-size: 14.5px; white-space: nowrap;
  }
  .address .label { color: var(--accent); }
</style>
</head>
<body>
<main class="stage">
  <section class="card card-front" aria-label="Card front">
    <div class="brand">
      <div class="brand-mark"></div>
      <div>
        <p class="brand-name">The Timber Loft</p>
        <p class="brand-tagline">Built to Fit Every Room</p>
      </div>
    </div>
    <p class="reg-number">Reg # 40582913</p>
  </section>

  <section class="card card-back" aria-label="Card back">
    <div class="identity">
      <h1 class="person-name">Adrian Kell</h1>
      <p class="person-role">CEO &amp; Founder</p>
    </div>
    <div class="divider"></div>
    <ul class="contacts">
      <li>
        <svg viewBox="0 0 14 14" aria-hidden="true"><rect x="3.5" y="1" width="7" height="12" rx="1.5" fill="none" stroke="#17a8e6" stroke-width="1.4"/><circle cx="7" cy="11" r="0.8" fill="#17a8e6"/></svg>
        <span>0207 555 0148</span>
      </li>
      <li>
        <svg viewBox="0 0 14 14" aria-hidden="true"><rect x="1" y="3" width="12" height="8.5" fill="#17a8e6"/><path d="M1 3 L7 8 L13 3" fill="none" stroke="#1d1d1e" stroke-width="1.2"/></svg>
        <span>info@<span class="accent">zorvelcabinets</span>.com</span>
      </li>
      <li>
        <svg viewBox="0 0 14 14" aria-hidden="true"><circle cx="7.5" cy="6" r="4.2" fill="none" stroke="#17a8e6" stroke-width="1.4"/><path d="M4.5 9 L1.5 12.5" stroke="#17a8e6" stroke-width="1.6"/></svg>
        <span>www.<span class="accent">zorvelcabinets</span>.com</span>
      </li>
    </ul>
    <p class="address"><span class="label">Address :</span> Unit 4, 27 Harrow Lane, London E2 7QP</p>
  </section>
</main>
</body>
</html>
```